Create a landing page for my local business that I’m looking to advertise

I own an oriental rug repair, restoration and cleaning business.
I’m looking to rug advertising and i would like a very clear *******UX and UI design******* website designed.

pages that i need:
-Repair and restoration
-Cleaning
-Blocking
-Staircase rug installation
_about us
-homepage
-our story
-contact us
-estimate

Www.velorantex.com

Industry/Entity Type

Rug Industry, Antique and New Rug Repair restoration and cleaning

Number of Pages Required

5+ page

Font styles to use
Serif
Sans Serif
Script

Colors
6B429C
8869AF
B7A5CE
E3DAEB
F3F0F8

Requirements
Must have
• IT HAS TO PRESENT FINE RUG REPAIR, RESTORATION AND CLEANING.
Should not have
• I DONT WANT THE WEBSITE TO LOOK LIKE A GENERIC “CLEANING COMPANY”. WE ARE A HIGH END RUG REPAIR ,RESTORATION AND CLEANING COMPANY

```html
<!DOCTYPE html>
<html lang="en">
<head>
<meta charset="utf-8">
<title>Velorantex Rugs — Luxury Custom Handmade Rugs</title>
<link rel="stylesheet" href="https://fonts.googleapis.com/css2?family=Alegreya:wght@400;500;700&family=Questrial&display=swap">
<style>
:root{
  --purple:#6B429C;
  --purple-mid:#8869AF;
  --purple-soft:#B7A5CE;
  --purple-pale:#E3DAEB;
  --purple-mist:#F3F0F8;
  --ink:#2b2b2b;
  --text:#444;
  --grey-bg:#f6f6f6;
  --white:#fff;
  --black:#000;
  --serif:'Alegreya',Georgia,serif;
  --sans:'Questrial',Arial,sans-serif;
}
*{margin:0;padding:0;box-sizing:border-box}
html,body{width:1200px;height:4942px;overflow:hidden}
body{position:relative;font-family:var(--sans);color:var(--text);background:var(--white)}
.abs{position:absolute}
.btn{position:absolute;display:flex;align-items:center;justify-content:center;font-family:var(--serif);font-size:17px;letter-spacing:.5px;text-transform:uppercase;background:var(--purple);color:var(--white)}
.label{font-family:var(--sans);font-size:12px;letter-spacing:1px;color:var(--purple-mid);text-transform:uppercase}
.title{font-family:var(--serif);font-weight:700;color:var(--ink);text-transform:uppercase;font-size:31px;line-height:1.2}
.rule{height:2px;width:98px;background:var(--ink)}
.copy{font-size:15px;line-height:27px;color:var(--text)}

/* hero */
.hero{left:0;top:0;width:1200px;height:637px;background:linear-gradient(160deg,#3a3632 0%,#6e6860 35%,#9b958c 65%,#8a8175 100%)}
.brand{display:flex;align-items:center;gap:10px;font-family:var(--serif);color:var(--white);font-size:19px;letter-spacing:1px}
.brand-dot{width:40px;height:40px;border:2px solid currentColor;border-radius:50%}
.nav{top:23px;left:624px;display:flex;align-items:center;font-family:var(--serif);font-size:12px;letter-spacing:.5px;color:var(--white);text-transform:uppercase}
.nav a{color:inherit;text-decoration:none;height:29px;display:flex;align-items:center}
.nav .active{color:var(--purple-soft)}
.nav .cta{background:var(--purple);padding:0 16px;height:29px}
.hero-title{position:absolute;left:628px;top:216px;width:460px;font-family:var(--serif);font-weight:700;font-size:43px;line-height:54px;color:var(--white)}
.hero-btn{left:628px;top:395px;width:167px;height:43px;background:var(--white);color:var(--purple)}

/* services */
.services{left:0;top:1162px;width:1200px;height:1747px;background:var(--grey-bg)}
.svc-img{position:absolute;width:402px;height:338px;border-radius:0 0 0 90px}
.svc-icon{position:absolute;width:150px;height:150px;border-radius:50%;background:var(--white);box-shadow:0 4px 18px rgba(0,0,0,.08);display:flex;align-items:center;justify-content:center}
.svc-text{position:absolute;width:350px}
.svc-text h3{font-family:var(--serif);font-weight:700;font-size:21px;color:var(--ink);margin-bottom:14px}
.svc-text .copy{font-size:14.5px}
.svc-text .btn{position:relative;margin-top:20px;width:169px;height:43px}

/* testimonial */
.quote-card{left:161px;top:3133px;width:878px;height:269px;background:var(--white);box-shadow:0 4px 24px rgba(0,0,0,.1);text-align:center;padding:62px 96px 0}
.quote-card p{font-style:italic;font-size:15px;line-height:30px;color:var(--text)}
.quote-card .who{font-family:var(--serif);font-style:italic;font-weight:700;color:var(--purple);margin-top:20px;font-size:16px}

/* banner */
.banner{left:0;top:3494px;width:1200px;height:452px;background:radial-gradient(ellipse at 40% 50%,#4a3a44 0%,#2c2028 50%,#1a1418 100%)}
.banner-title{left:0;top:3650px;width:1200px;text-align:center;font-family:var(--serif);font-weight:400;font-size:34px;line-height:44px;color:var(--white)}
.ghost{position:absolute;left:486px;top:3744px;width:226px;height:44px;border:1px solid var(--white);color:var(--white);font-family:var(--serif);font-size:17px;display:flex;align-items:center;justify-content:center;letter-spacing:.5px}

/* contact */
.footer{left:0;top:4604px;width:1200px;height:338px;background:var(--black)}
.contact-panel{left:161px;top:4032px;width:488px;height:620px;background:var(--purple)}
.map{left:180px;top:4051px;width:450px;height:298px;background:linear-gradient(135deg,#e9e7e4,#d9d6d2)}
.info{position:absolute;left:178px;display:flex;align-items:center;gap:22px;color:var(--white)}
.info .ring{width:50px;height:50px;border:1.5px solid rgba(255,255,255,.7);border-radius:50%;display:flex;align-items:center;justify-content:center}
.info b{display:block;font-family:var(--sans);font-size:16px;font-weight:700}
.info span{font-size:14px}
.form-title{left:691px;top:4042px;font-family:var(--serif);font-weight:700;font-size:31px;color:var(--ink);text-transform:uppercase;letter-spacing:.5px}
.field{position:absolute;left:691px;width:348px;height:37px;border:1px solid #e1e1e1;background:var(--white);font-size:12px;color:#666;padding:0 22px;display:flex;align-items:center;justify-content:space-between}
.field.msg{height:111px;align-items:flex-start;padding-top:14px}
.submit{left:691px;top:4516px;width:348px;height:42px}

.foot-nav{left:0;top:4826px;width:1200px;display:flex;justify-content:center;gap:54px;font-family:var(--sans);font-weight:700;font-size:12px;color:var(--white);letter-spacing:.5px}
.foot-nav .active{color:var(--purple-soft)}
.copyright{left:0;top:4898px;width:1200px;text-align:center;color:var(--white);font-size:12px}
</style>
</head>
<body>

<!-- hero -->
<section class="abs hero" role="img" aria-label="Handmade rug with a radiating pattern under a chair on a wooden floor"></section>
<div class="abs brand" style="left:161px;top:17px;"><span class="brand-dot"></span>VELORANTEX</div>
<nav class="abs nav">
  <a class="active" style="margin-right:45px">Home</a>
  <a style="margin-right:45px">About Us</a>
  <a style="margin-right:45px">Services</a>
  <a class="cta">Contact Us</a>
</nav>
<h1 class="hero-title">We are a Luxury Custom Handmade Rugs Company.</h1>
<a class="btn hero-btn">Contact Us</a>

<!-- about -->
<div class="abs label" style="left:161px;top:726px">About Us</div>
<h2 class="abs title" style="left:161px;top:744px;font-size:30px;line-height:38px">Welcome to<br>Velorantex Rugs</h2>
<p class="abs" style="left:161px;top:846px;width:450px;font-weight:700;font-size:15.5px;line-height:22px;color:var(--purple)">Lorem ipsum dolor sit amet, conse ctetuer adipiscing elit, sed diam no nummy nibh</p>
<p class="abs copy" style="left:161px;top:906px;width:455px">Lorem ipsum dolor sit amet, consectetuer adipiscing elit, sed diam nonummy nibh euismod tincidunt ut laoreet dolore magna aliquam erat volutpat. Ut wisi enim ad minim veniam, quis nostrud exerci tation ullamcorper.</p>
<a class="btn" style="left:161px;top:1033px;width:169px;height:44px">Read More</a>
<div class="abs" role="img" aria-label="Close-up of rug restoration work on an antique rug" style="left:636px;top:760px;width:403px;height:300px;background:linear-gradient(135deg,#5a5560,#9a8f8c 50%,#b58a74)"></div>

<!-- services -->
<section class="abs services"></section>
<div class="abs label" style="left:0;width:1200px;text-align:center;top:1251px">Services</div>
<h2 class="abs title" style="left:0;width:1200px;text-align:center;top:1268px">What We Do</h2>
<div class="abs rule" style="left:551px;top:1313px"></div>

<div class="svc-img" role="img" aria-label="Antique rug with a hole prepared for repair" style="left:161px;top:1354px;background:linear-gradient(135deg,#3f5a7a,#a8443a 50%,#c8a37a)"></div>
<div class="svc-icon" style="left:488px;top:1448px">
  <svg width="70" height="70" viewBox="0 0 70 70" fill="none" stroke="#6B429C" stroke-width="3"><rect x="14" y="18" width="26" height="36" rx="3"/><line x1="10" y1="18" x2="44" y2="18"/><line x1="10" y1="54" x2="44" y2="54"/><line x1="18" y1="26" x2="36" y2="26"/><line x1="18" y1="34" x2="36" y2="34"/><line x1="18" y1="42" x2="36" y2="42"/><line x1="60" y1="10" x2="46" y2="58"/></svg>
</div>
<div class="svc-text" style="left:687px;top:1390px">
  <h3>Repair and Restoration</h3>
  <p class="copy">Lorem ipsum dolor sit amet, consectetuer adipiscing elit, sed diam nonummy nibh euismod tincidunt ut laoreet dolore magna aliquam erat volutpat. Ut wisi enim ad minim veniam, quis nostrud exerci tation ullamcorper suscipit lobortis nisl.</p>
  <a class="btn">Contact Us</a>
</div>

<div class="svc-text" style="left:161px;top:1765px">
  <h3>Cleaning</h3>
  <p class="copy">Lorem ipsum dolor sit amet, consectetuer adipiscing elit, sed diam nonummy nibh euismod tincidunt ut laoreet dolore magna aliquam erat volutpat. Ut wisi enim ad minim veniam, quis nostrud exerci tation ullamcorper suscipit lobortis nisl.</p>
  <a class="btn">Contact Us</a>
</div>
<div class="svc-img" role="img" aria-label="Rug being hand washed with a brush and foam" style="left:637px;top:1729px;background:linear-gradient(135deg,#1f2c40,#4b5f80 55%,#c9cfd8)"></div>
<div class="svc-icon" style="left:562px;top:1823px">
  <svg width="70" height="70" viewBox="0 0 70 70" fill="none" stroke="#6B429C" stroke-width="3"><rect x="14" y="16" width="38" height="28"/><line x1="14" y1="52" x2="52" y2="52"/><line x1="20" y1="44" x2="20" y2="58"/><line x1="28" y1="44" x2="28" y2="58"/><line x1="36" y1="44" x2="36" y2="58"/><line x1="44" y1="44" x2="44" y2="58"/><path d="M56 10l2 4 4 2-4 2-2 4-2-4-4-2 4-2z"/></svg>
</div>

<div class="svc-img" role="img" aria-label="Rug edge being rewoven with warp threads" style="left:161px;top:2104px;background:linear-gradient(135deg,#8c8a80,#a53a32 50%,#2e3e5e)"></div>
<div class="svc-icon" style="left:488px;top:2198px">
  <svg width="70" height="70" viewBox="0 0 70 70" fill="none" stroke="#6B429C" stroke-width="3"><path d="M12 44h46v10H12z"/><line x1="18" y1="54" x2="18" y2="60"/><line x1="26" y1="54" x2="26" y2="60"/><line x1="34" y1="54" x2="34" y2="60"/><line x1="42" y1="54" x2="42" y2="60"/><line x1="50" y1="54" x2="50" y2="60"/><path d="M22 40l18-24 8 6-14 18"/></svg>
</div>
<div class="svc-text" style="left:687px;top:2140px">
  <h3>Blocking</h3>
  <p class="copy">Lorem ipsum dolor sit amet, consectetuer adipiscing elit, sed diam nonummy nibh euismod tincidunt ut laoreet dolore magna aliquam erat volutpat. Ut wisi enim ad minim veniam, quis nostrud exerci tation ullamcorper suscipit lobortis nisl.</p>
  <a class="btn">Contact Us</a>
</div>

<div class="svc-text" style="left:161px;top:2515px">
  <h3>Staircase Rug Installation</h3>
  <p class="copy">Lorem ipsum dolor sit amet, consectetuer adipiscing elit, sed diam nonummy nibh euismod tincidunt ut laoreet dolore magna aliquam erat volutpat. Ut wisi enim ad minim veniam, quis nostrud exerci tation ullamcorper suscipit lobortis nisl.</p>
  <a class="btn">Contact Us</a>
</div>
<div class="svc-img" role="img" aria-label="Patterned runner rug installed on a staircase" style="left:637px;top:2479px;background:linear-gradient(90deg,#d8d2ca,#3a1c20 25%,#5a2a2c 60%,#e6e1da)"></div>
<div class="svc-icon" style="left:562px;top:2573px">
  <svg width="70" height="70" viewBox="0 0 70 70" fill="none" stroke="#8869AF" stroke-width="3"><rect x="26" y="18" width="18" height="8"/><rect x="21" y="26" width="28" height="8"/><rect x="16" y="34" width="38" height="8"/><rect x="11" y="42" width="48" height="8"/></svg>
</div>

<!-- testimonials -->
<div class="abs label" style="left:0;width:1200px;text-align:center;top:2994px">Reviews</div>
<h2 class="abs title" style="left:0;width:1200px;text-align:center;top:3012px">Client Testimonials</h2>
<div class="abs rule" style="left:551px;top:3057px"></div>
<div class="abs quote-card">
  <p>Lorem ipsum dolor sit amet, consectetuer adipiscing elit, sed diam nonummy nibh euismod tincidunt ut laoreet dolore magna aliquam erat volutpat. Ut wisi enim ad minim veniam, quis nostrud exerci tation ullamcorper suscipit lobortis nisl ut aliquip ex ea commodo consequat. Duis autem vel eum iriure dolor in hendrerit in vulputate velit esse molestie consequat.</p>
  <div class="who">- Marian, 73</div>
</div>
<svg class="abs" style="left:553px;top:3094px" width="94" height="74" viewBox="0 0 94 74"><path fill="#8869AF" d="M4 70V44C4 20 14 6 38 0l4 8C28 14 22 24 22 36h18v34zM52 70V44C52 20 62 6 86 0l4 8C76 14 70 24 70 36h18v34z"/></svg>
<svg class="abs" style="left:131px;top:3258px" width="74" height="20" viewBox="0 0 74 20" fill="none" stroke="#666" stroke-width="2"><line x1="2" y1="10" x2="72" y2="10"/><path d="M12 2L2 10l10 8"/></svg>
<svg class="abs" style="left:995px;top:3258px" width="74" height="20" viewBox="0 0 74 20" fill="none" stroke="#6B429C" stroke-width="2.5"><line x1="2" y1="10" x2="72" y2="10"/><path d="M62 2l10 8-10 8"/></svg>

<!-- banner -->
<section class="abs banner" role="img" aria-label="Dark close-up of a hand-knotted oriental rug"></section>
<h2 class="abs banner-title">Antique, New Rug Repair,<br>Restoration And Cleaning</h2>
<a class="ghost">GET A FREE ESTIMATE</a>

<!-- contact & footer -->
<footer class="abs footer"></footer>
<div class="abs contact-panel"></div>
<div class="abs map" role="img" aria-label="Street map showing the workshop location"></div>
<svg class="abs" style="left:386px;top:4145px" width="40" height="56" viewBox="0 0 40 56"><path fill="#6B429C" d="M20 0a20 20 0 0 1 20 20c0 14-20 36-20 36S0 34 0 20A20 20 0 0 1 20 0z"/><circle cx="20" cy="20" r="11" fill="#fff"/></svg>

<div class="info" style="top:4391px">
  <div class="ring"><svg width="20" height="24" viewBox="0 0 20 24" fill="none" stroke="#fff" stroke-width="1.6"><path d="M10 23S2 14 2 9a8 8 0 0 1 16 0c0 5-8 14-8 14z"/><circle cx="10" cy="9" r="3"/></svg></div>
  <div><b>Address</b><span>123, Building Name, Street, City, State XY 123456</span></div>
</div>
<div class="info" style="top:4462px">
  <div class="ring"><svg width="22" height="16" viewBox="0 0 22 16" fill="none" stroke="#fff" stroke-width="1.6"><rect x="1" y="1" width="20" height="14"/><path d="M1 1l10 8 10-8"/></svg></div>
  <div><b>Email</b><span>info@velorantex.com</span></div>
</div>
<div class="info" style="top:4533px">
  <div class="ring"><svg width="20" height="20" viewBox="0 0 20 20" fill="none" stroke="#fff" stroke-width="1.6"><path d="M4 1l4 4-2 3c1 3 3 5 6 6l3-2 4 4-3 3C8 19 1 12 1 4z"/></svg></div>
  <div><b>Phone</b><span>123 456 7890</span></div>
</div>

<h2 class="abs form-title">Get In Touch</h2>
<div class="field" style="top:4116px">First Name</div>
<div class="field" style="top:4168px">Last Name</div>
<div class="field" style="top:4220px">Phone</div>
<div class="field" style="top:4273px">Email</div>
<div class="field" style="top:4325px">Enquiry For <svg width="12" height="8" viewBox="0 0 12 8"><path d="M0 0h12L6 8z" fill="#333"/></svg></div>
<div class="field msg" style="top:4378px">Message</div>
<a class="btn submit">Submit</a>

<div class="abs brand" style="left:493px;top:4730px;font-size:24px;color:var(--purple-mid)"><span class="brand-dot" style="width:56px;height:56px"></span>VELORANTEX</div>
<nav class="abs foot-nav"><span class="active">HOME</span><span>ABOUT US</span><span>SERVICES</span><span>CONTACT US</span></nav>
<p class="abs copyright">Copyright © 2021 Velorantex Rugs. All Rights Reserved.</p>

</body>
</html>
```